Gentle Willow Pregnancy and Baby Massage

I need a web design for a new business, GENTLE WILLOW PREGNANCY AND BABY MASSAGE that I am in the process of setting up in the suburbs of Perth, Western Australia. The business is owned and operated by myself and my intention is to service Pregnant Mothers and Parents of Young Babies that would benefit from massage. I would like to have a "Home Page" and pages for "About Me", "Pregnancy Massage", "Baby Massage", a Pricing Page for Pregnancy Massage Sessions, a Pricing Page for Baby Massage Sessions, and a "Contact Me" page to allow clients to either contact me with queries or book available pregnancy massage sessions on a particular day of the week. I would also like a "News" page that would include articles I have written, news about new courses and a link to my Chatterlane page (yet to be set up). I would like to keep the colour schemes similar to my logo design colours. I need the design to be easy to follow and to appeal to a younger audience (20's to mid 30's).
The target audience is pregnant mothers-to-be wishing to receive massage treatments, and new parents and grandparents of small babies that would like to learn how to massage their babies.
The look and feel should be modern, professional, elegant and feminine.
I need the design to be in a standard format such that I can update the content by myself ( and does not need specialised software) as the company and business progresses.

Target Market(s)

Industry/Entity Type

Health And Wellness

Contact Information for Business Card

Card should have rounded edges. Design should have the same "feel" as the website. Contact Details of my business address, mobile phone, email and website should be included.

Coding

Coded - Design and coding required

Number of Pages Required

5+ page

Font styles to use
Script

Requirements
Must have
• Same colours as logo design. In cmyk system, the colours are: 20,60,0,0 which best result is tintora 681 and 40,40,0,0 which best result is tintora 2645. Card should include the logo design.

```html
<!DOCTYPE html>
<html lang="en">
<head>
<meta charset="utf-8">
<title>About Me – Gentle Willow Pregnancy and Baby Massage</title>
<link rel="stylesheet" href="https://fonts.googleapis.com/css2?family=PT+Sans:wght@400;700&family=Source+Sans+3:wght@600;700&family=Parisienne&display=swap">
<style>
  :root {
    --plum: #b86fa4;
    --plum-deep: #a1609a;
    --lavender: #8d80b8;
    --lavender-soft: #c3bbdd;
    --blush: #fbe6f2;
    --blush-soft: #fdf2f8;
    --heart: #f29ab8;
    --ink: #2b2b2b;
    --rule: #dcd6ea;
    --white: #ffffff;
  }
  * { box-sizing: border-box; margin: 0; padding: 0; }
  html, body { width: 1069px; height: 1200px; overflow: hidden; }
  body {
    position: relative;
    background: var(--white);
    font-family: "PT Sans", Arial, sans-serif;
    color: var(--ink);
  }

  /* Header + banner */
  .hero {
    position: absolute; left: 0; top: 0; width: 1069px; height: 280px;
    background: linear-gradient(180deg, var(--blush-soft) 0%, var(--blush) 100%);
  }
  .hero-pattern {
    position: absolute; left: 0; top: 115px; width: 1069px; height: 165px;
    background: linear-gradient(180deg, #f9e1ef 0%, #fae4f1 50%, #f8ddec 100%);
  }
  .brand {
    position: absolute; left: 182px; top: 30px;
    display: flex; align-items: center; gap: 8px;
  }
  .brand-dot { width: 18px; height: 18px; border-radius: 50%; background: var(--plum); }
  .brand-name {
    font-family: "PT Sans", Arial, sans-serif; font-weight: 700;
    color: var(--plum-deep); font-size: 16px; line-height: 1.15;
  }
  .main-nav {
    position: absolute; left: 387px; top: 63px;
    display: flex; gap: 25px;
    font-family: "Source Sans 3", Arial, sans-serif; font-weight: 700;
    font-size: 13.5px; letter-spacing: 0.2px;
  }
  .main-nav a { text-decoration: none; color: var(--plum); }
  .main-nav a.is-active { color: var(--lavender); }
  .social-top { position: absolute; left: 824px; top: 52px; display: flex; gap: 6px; }
  .heart { width: 22px; height: 20px; }
  .heart path { fill: var(--heart); }
  .page-title {
    position: absolute; left: 0; top: 160px; width: 1069px; text-align: center;
    font-family: "Parisienne", cursive; font-weight: 400; font-size: 50px; color: #1c1c1c;
  }

  /* About */
  .portrait {
    position: absolute; left: 219px; top: 322px; width: 269px; height: 290px;
    background: linear-gradient(160deg, #e9e9eb 0%, #dcdde0 55%, #2f5f8f 56%, #2a5a8a 100%);
  }
  .bio {
    position: absolute; left: 515px; top: 328px; width: 380px;
    font-size: 12.4px; line-height: 19.3px;
  }
  .bio p + p.gap { margin-top: 19.3px; }
  .divider { position: absolute; left: 0; top: 687px; width: 1069px; height: 1px; background: var(--rule); }

  /* Testimonial */
  .testimonial-photo {
    position: absolute; left: 538px; top: 743px; width: 96px; height: 96px; border-radius: 50%;
    border: 3px solid #f6dcea;
    background: radial-gradient(circle at 55% 45%, #f1d2bd 0%, #e8c1a4 45%, #c89a7c 100%);
  }
  .testimonial-quote {
    position: absolute; left: 320px; top: 855px; width: 510px; text-align: center;
    font-size: 12.8px; line-height: 16.4px;
  }
  .testimonial-name {
    position: absolute; left: 0; top: 910px; width: 1148px; text-align: center;
    font-family: "Source Sans 3", Arial, sans-serif; font-weight: 600; font-size: 15px; color: var(--lavender);
  }
  .slider-dots { position: absolute; left: 552px; top: 939px; display: flex; gap: 9px; }
  .slider-dots span { width: 8px; height: 8px; border-radius: 50%; background: #e4e1ec; }
  .slider-dots span.is-active { background: #b9b0d8; }

  /* Footer */
  .site-footer {
    position: absolute; left: 0; top: 994px; width: 1069px; height: 175px;
    background: var(--lavender-soft); color: var(--white);
  }
  .cert-badge { position: absolute; left: 266px; top: 32px; width: 88px; height: 50px; background: var(--white); }
  .cert-text { position: absolute; left: 266px; top: 91px; width: 200px; font-size: 10px; line-height: 12.8px; }
  .footer-heading {
    position: absolute; top: 29px; font-family: "Source Sans 3", Arial, sans-serif;
    font-weight: 700; font-size: 12.5px; letter-spacing: 1.5px;
  }
  .footer-heading.contact { left: 496px; }
  .footer-heading.connect { left: 750px; }
  .contact-lines { position: absolute; left: 495px; top: 51px; font-size: 11.8px; line-height: 15.5px; }
  .contact-lines strong { font-weight: 700; }
  .social-foot { position: absolute; left: 750px; top: 54px; display: flex; gap: 8px; }
  .social-foot .heart { width: 25px; height: 23px; }
  .copyright {
    position: absolute; left: 0; top: 1169px; width: 1069px; height: 31px;
    background: var(--plum); color: var(--white); text-align: center;
    font-family: Georgia, serif; font-size: 10.5px; line-height: 31px;
  }
</style>
</head>
<body>
  <header class="hero">
    <div class="hero-pattern" role="img" aria-label="Soft pink wavy line pattern"></div>
    <div class="brand">
      <span class="brand-dot"></span>
      <span class="brand-name">Gentle Willow<br>Pregnancy and Baby Massage</span>
    </div>
    <nav class="main-nav">
      <a href="#">HOME</a>
      <a href="#" class="is-active">ABOUT ME</a>
      <a href="#">BENEFITS</a>
      <a href="#">MASSAGE</a>
      <a href="#">CONTACT</a>
    </nav>
    <div class="social-top" aria-label="Social links">
      <svg class="heart" viewBox="0 0 22 20"><path d="M11 19 C4 13 0 10 0 5.5 A5.5 5.5 0 0 1 11 4 A5.5 5.5 0 0 1 22 5.5 C22 10 18 13 11 19Z"/></svg>
      <svg class="heart" viewBox="0 0 22 20"><path d="M11 19 C4 13 0 10 0 5.5 A5.5 5.5 0 0 1 11 4 A5.5 5.5 0 0 1 22 5.5 C22 10 18 13 11 19Z"/></svg>
      <svg class="heart" viewBox="0 0 22 20"><path d="M11 19 C4 13 0 10 0 5.5 A5.5 5.5 0 0 1 11 4 A5.5 5.5 0 0 1 22 5.5 C22 10 18 13 11 19Z"/></svg>
      <svg class="heart" viewBox="0 0 22 20"><path d="M11 19 C4 13 0 10 0 5.5 A5.5 5.5 0 0 1 11 4 A5.5 5.5 0 0 1 22 5.5 C22 10 18 13 11 19Z"/></svg>
    </div>
    <h1 class="page-title">About Me</h1>
  </header>

  <main>
    <div class="portrait" role="img" aria-label="Portrait photo of Maren, the massage practitioner"></div>
    <section class="bio">
      <p>Maren is a Practitioner of Pregnancy Massage, and a Paediatric Massage Consultant. She completed her training with Bloom Prenatal Training, and the Infant Touch Learning Network. The ITLN is endorsed by the Coastal College of Midwives. The Heritage Remedies Society, and accredited by the Guild of Massage Therapists.</p>
      <p class="gap">Maren is also a Registered Nurse and Midwife. Most of her professional career has been as a midwife, which has included working in the community in the UK, providing ante natal care and classes, intra partum care, home births, and postnatal care in the home. Maren has also worked in the private and public maternity sectors in Perth.</p>
      <p>Maren was introduced to the wonderful benefits of pregnancy and baby massage after a career change. Working as a Practitioner of Pregnancy Massage, and Paediatric Massage Consultant, enables her to continue working with mothers and babies.</p>
    </section>
    <div class="divider"></div>

    <section class="testimonial">
      <div class="testimonial-photo" role="img" aria-label="Round photo of a smiling mother holding her baby"></div>
      <p class="testimonial-quote">Lorem Ipsum is simply dummy text of the printing and typesetting industry. Lorem Ipsum has been the industry's standard dummy text ever since the 1500s, when an unknown printer took a galley of type and scrambled</p>
      <p class="testimonial-name">Clara Dunne</p>
      <div class="slider-dots"><span></span><span class="is-active"></span><span></span></div>
    </section>
  </main>

  <footer class="site-footer">
    <div class="cert-badge" role="img" aria-label="Certification badge"></div>
    <p class="cert-text">The ITLN is endorsed by the Coastal College of Midwives. The Heritage Remedies Society, and accredited by the Guild of Massage Therapists.</p>
    <h2 class="footer-heading contact">CONTACT</h2>
    <div class="contact-lines">
      <strong>Gentle Willow Pregnancy and Infant Massage</strong><br>
      <strong>Email</strong>: maren.ellis@gentle-willow.com.au<br>
      <strong>Telephone</strong> : 041 5550 372
    </div>
    <h2 class="footer-heading connect">CONNECT</h2>
    <div class="social-foot" aria-label="Social links">
      <svg class="heart" viewBox="0 0 22 20"><path d="M11 19 C4 13 0 10 0 5.5 A5.5 5.5 0 0 1 11 4 A5.5 5.5 0 0 1 22 5.5 C22 10 18 13 11 19Z"/></svg>
      <svg class="heart" viewBox="0 0 22 20"><path d="M11 19 C4 13 0 10 0 5.5 A5.5 5.5 0 0 1 11 4 A5.5 5.5 0 0 1 22 5.5 C22 10 18 13 11 19Z"/></svg>
      <svg class="heart" viewBox="0 0 22 20"><path d="M11 19 C4 13 0 10 0 5.5 A5.5 5.5 0 0 1 11 4 A5.5 5.5 0 0 1 22 5.5 C22 10 18 13 11 19Z"/></svg>
      <svg class="heart" viewBox="0 0 22 20"><path d="M11 19 C4 13 0 10 0 5.5 A5.5 5.5 0 0 1 11 4 A5.5 5.5 0 0 1 22 5.5 C22 10 18 13 11 19Z"/></svg>
    </div>
  </footer>
  <div class="copyright">Copyright gentlewillow.com</div>
</body>
</html>
```